KRT World Class Organisation Poster

We are looking for ideas on how to design this poster to best capture the message we are trying to convey (KRT World Class Organisation). Make sure that these 5 statements feature on the poster.

Logo has been provided, please include in your poster design.

Please use the logo design as the inspiration for your poster layout, drawing on the DNA double helix symbol.

Also refer to the layout of the attached poster. We would like to retain the layout however it should be visually appealing - use your imagination & creativity!
Updates

Updated design brief & extended deadline.

Target Market(s)

internal company use only - logo provided which will need to be included.

Requirements
Must have
• The poster should be in portrait format as it will be printed in 'A3' size.

Must include the KRT logo provided - see attached file.
Nice to have
• Please use the logo design as the inspiration for your poster layout, drawing on the DNA double helix symbol.

```html
<!DOCTYPE html>
<html lang="en">
<head>
<meta charset="utf-8">
<title>KRT World Class Organisation Poster</title>
<link href="https://fonts.googleapis.com/css2?family=Signika:wght@300;400;600&family=PT+Sans:wght@400;700&display=swap" rel="stylesheet">
<style>
  :root {
    --page: #ffffff;
    --navy: #07315e;
    --navy-deep: #062b54;
    --blue-mid: #1a5a9a;
    --blue-light: #6fb3e6;
    --title-dark: #0b3566;
    --title-soft: #3b6b9e;
    --ring: #9fd0f0;
    --text: #ffffff;
  }
  * { margin: 0; padding: 0; box-sizing: border-box; }
  html, body { width: 1200px; height: 900px; overflow: hidden; background: var(--page); }
  .canvas { position: relative; width: 1200px; height: 900px; }
  .poster {
    position: absolute; left: 317px; top: 50px; width: 566px; height: 800px;
    background: var(--navy);
    box-shadow: 2px 3px 8px rgba(0,0,0,0.25);
    overflow: hidden;
  }
  .header-art {
    position: absolute; left: 0; top: 0; width: 100%; height: 330px;
    background:
      linear-gradient(to bottom,
        rgba(120,190,240,0.9) 0px,
        rgba(255,255,255,0.95) 40px,
        #ffffff 130px,
        #ffffff 150px,
        #8fc3ea 190px,
        var(--blue-mid) 240px,
        var(--navy) 330px);
  }
  .title { position: absolute; font-family: "Signika", sans-serif; line-height: 1; }
  .title-lead { left: 46px; top: 36px; font-size: 40px; font-weight: 400; color: var(--title-soft); letter-spacing: -0.5px; }
  .title-main { left: 110px; top: 70px; font-size: 68px; font-weight: 600; color: var(--title-dark); letter-spacing: -1.5px; }
  .title-tail { right: 48px; top: 128px; font-size: 38px; font-weight: 300; color: var(--title-soft); }
  .rings { position: absolute; left: 0; top: 0; }
  .statement {
    position: absolute; transform: translate(-50%, -50%);
    font-family: "PT Sans", sans-serif; font-size: 11px; line-height: 13px;
    color: var(--text); text-align: center;
  }
  .statement b { font-weight: 700; }
  .statement .num { font-size: 14px; font-weight: 700; }
</style>
</head>
<body>
<div class="canvas">
  <section class="poster">
    <div class="header-art" role="img" aria-label="Blue circuit board pattern fading into white behind the title"></div>

    <h1>
      <span class="title title-lead">KRT is a</span>
      <span class="title title-main">World Class</span>
      <span class="title title-tail">organisation</span>
    </h1>

    <svg class="rings" width="566" height="800" viewBox="0 0 566 800" aria-hidden="true">
      <defs>
        <filter id="glow" x="-30%" y="-30%" width="160%" height="160%">
          <feGaussianBlur stdDeviation="4"/>
        </filter>
      </defs>
      <g stroke="var(--blue-light)" stroke-width="1.2">
        <line x1="190" y1="440" x2="205" y2="452"/>
        <line x1="366" y1="430" x2="383" y2="416"/>
        <line x1="190" y1="612" x2="206" y2="597"/>
        <line x1="366" y1="590" x2="385" y2="606"/>
      </g>
      <g fill="none" stroke="var(--ring)">
        <g stroke-width="9" opacity="0.55" filter="url(#glow)">
          <circle cx="120" cy="382" r="80"/>
          <circle cx="443" cy="355" r="86"/>
          <circle cx="285" cy="515" r="106"/>
          <circle cx="126" cy="673" r="90"/>
          <circle cx="443" cy="660" r="76"/>
        </g>
        <g stroke-width="2.5" opacity="0.8">
          <circle cx="120" cy="382" r="80"/>
          <circle cx="443" cy="355" r="86"/>
          <circle cx="285" cy="515" r="106"/>
          <circle cx="126" cy="673" r="90"/>
          <circle cx="443" cy="660" r="76"/>
        </g>
      </g>
    </svg>

    <p class="statement" style="left:120px; top:382px; width:125px;">
      <span class="num">1.</span> We employ<br><b>World Class Business Systems</b> to exceed expectations by driving innovation at the forefront of technology.
    </p>
    <p class="statement" style="left:443px; top:357px; width:128px;">
      <span class="num">2.</span> We manufacture using innovative <b>World Class Manufacturing Processes</b> and lean technologies adapted to produce safe, effective &amp; reliable products to meet our patients' needs.
    </p>
    <p class="statement" style="left:285px; top:518px; width:172px;">
      <span class="num">3.</span> We strive to be<br><b>World Class Colleagues</b><br>who are professional, motivated, helpful and positive. We are accountable in achieving our goals. We are innovative, always challenge the status-quo and open to new ideas.
    </p>
    <p class="statement" style="left:126px; top:676px; width:130px;">
      <span class="num">4.</span> We work with<br><b>World Class Service Providers</b> who are leaders and innovators that challenge the status-quo and focus on quality excellence and continuous improvement to exceed customer expectations.
    </p>
    <p class="statement" style="left:443px; top:660px; width:122px;">
      <span class="num">5.</span> We believe<br><b>World Class Customer Service</b> is to deliver the ultimate customer satisfaction every time.
    </p>
  </section>
</div>
</body>
</html>
```